Business Card Design

Recruitment Company. Want to keep the logo and the green colour

Industry/Entity Type

Business

Contact Information for Business Card

Hi,

1.)
MARTIN COLLARD
Director
Level 4, 238 Finch Terrace
Brisbane QLD 4000
M 0412 604 337
E martin@paceltalent.com.au
www.paceltalent.com.au

2.)
TOM WHITFORD
Director
Level 4, 238 Finch Terrace
Brisbane QLD 4000
M 0419 572 641
E tom@paceltalent.com.au

Want something different and eye catching, happy for you guys to use your design flare to work some magic with these.

Many Thanks
Tom

```html
<!DOCTYPE html>
<html lang="en">
<head>
<meta charset="utf-8">
<title>Pacel Talent – Business Card</title>
<link rel="stylesheet" href="https://fonts.googleapis.com/css2?family=Open+Sans:wght@400;600;700&display=swap">
<style>
  :root {
    --backdrop: #e9e5df;
    --card: #f7f8f6;
    --card-edge: #dfe3de;
    --brand-green: #5a9a2a;
    --brand-green-dark: #3f7d1f;
    --brand-green-light: #8cbf3a;
    --ink: #2e2e2e;
    --accent-bar: #2a2a2a;
  }
  * { margin: 0; padding: 0; box-sizing: border-box; }
  html, body {
    width: 1200px;
    height: 969px;
    overflow: hidden;
    background: var(--backdrop);
    font-family: "Open Sans", Arial, sans-serif;
  }
  .canvas {
    position: relative;
    width: 1200px;
    height: 969px;
  }
  .business-card {
    position: absolute;
    left: 180px;
    top: 246px;
    width: 840px;
    height: 477px;
    background: var(--card);
    border: 1px solid var(--card-edge);
    border-radius: 22px;
    box-shadow: 0 14px 40px rgba(0, 0, 0, 0.12);
    overflow: hidden;
  }
  .accent-bar {
    position: absolute;
    left: 0;
    top: 217px;
    width: 13px;
    height: 68px;
    background: var(--accent-bar);
  }
  .company-name {
    position: absolute;
    left: 46px;
    top: 88px;
    font-size: 60px;
    font-weight: 700;
    line-height: 1;
    color: var(--brand-green);
    letter-spacing: -1px;
  }
  .brand-emblem {
    position: absolute;
    left: 480px;
    top: 70px;
    width: 320px;
    height: 320px;
    border-radius: 50%;
    background: radial-gradient(circle at 40% 35%, var(--brand-green-light), var(--brand-green) 70%);
  }
  .person-name {
    position: absolute;
    left: 48px;
    top: 223px;
    font-size: 28px;
    font-weight: 700;
    color: var(--brand-green-dark);
    letter-spacing: 0.5px;
  }
  .person-title {
    position: absolute;
    left: 48px;
    top: 264px;
    font-size: 21px;
    font-weight: 400;
    color: var(--ink);
  }
  .contact-list {
    position: absolute;
    left: 48px;
    top: 312px;
    list-style: none;
  }
  .contact-item {
    display: flex;
    align-items: center;
    height: 32px;
    font-size: 19px;
    color: var(--ink);
  }
  .contact-icon {
    width: 18px;
    height: 18px;
    margin-right: 12px;
    fill: var(--brand-green);
    flex: none;
  }
  .address {
    position: absolute;
    left: 48px;
    top: 418px;
    font-size: 19px;
    color: var(--ink);
  }
</style>
</head>
<body>
<div class="canvas">
  <div class="business-card">
    <div class="accent-bar"></div>
    <div class="company-name">pacel talent</div>

    <div class="brand-emblem" role="img" aria-label="Large brand emblem in green"></div>

    <div class="person-name">MARTIN COLLARD</div>
    <div class="person-title">Director</div>

    <ul class="contact-list">
      <li class="contact-item">
        <svg class="contact-icon" viewBox="0 0 18 18" aria-hidden="true">
          <path d="M5 1h8a1.5 1.5 0 0 1 1.5 1.5v13A1.5 1.5 0 0 1 13 17H5a1.5 1.5 0 0 1-1.5-1.5v-13A1.5 1.5 0 0 1 5 1zm0.5 2v10.5h7V3z"/>
        </svg>
        0412 604 337
      </li>
      <li class="contact-item">
        <svg class="contact-icon" viewBox="0 0 18 18" aria-hidden="true">
          <path d="M1 4h16v1.2L9 10 1 5.2z M1 6.8l8 4.8 8-4.8V14H1z"/>
        </svg>
        martin@paceltalent.com.au
      </li>
      <li class="contact-item">
        <svg class="contact-icon" viewBox="0 0 18 18" aria-hidden="true">
          <path d="M9 1a8 8 0 1 0 0 16A8 8 0 0 0 9 1zm0 1.6c.9 0 1.9 1.6 2.3 4.1H6.7C7.1 4.2 8.1 2.6 9 2.6zM2.8 6.7a6.4 6.4 0 0 1 2.6-3.2c-.5 1-.8 2-.9 3.2zm-.2 1.6h1.8a14 14 0 0 0 0 1.4H2.6zm.2 3h1.7c.1 1.2.4 2.2.9 3.2a6.4 6.4 0 0 1-2.6-3.2zM9 15.4c-.9 0-1.9-1.6-2.3-4.1h4.6c-.4 2.5-1.4 4.1-2.3 4.1zm-2.5-5.7a12 12 0 0 1 0-1.4h5a12 12 0 0 1 0 1.4zm6.1 4.8c.5-1 .8-2 .9-3.2h1.7a6.4 6.4 0 0 1-2.6 3.2zm1-4.8a14 14 0 0 0 0-1.4h1.8a6 6 0 0 1 0 1.4zm-.1-3c-.1-1.2-.4-2.2-.9-3.2a6.4 6.4 0 0 1 2.6 3.2z"/>
        </svg>
        www.paceltalent.com.au
      </li>
    </ul>

    <div class="address">Level 4, 238 Finch Terrace, Brisbane QLD 4000</div>
  </div>
</div>
</body>
</html>
```